Quiet Porch : Wasp Trap 19x7.5x31cm ( USE THE DIELIENES)

We are seeking a creative and skilled designer to create an innovative packaging design for our brand "Quiet Porch," which specializes in eco-friendly, safe, and effective pest control solutions. Our brand Quiet Porch is deeply rooted in sustainability, safety, and enhancing the living environment, and we aim to communicate these values through our packaging design.

Please take a look at the files for the cuttinglines ( dielines) and futher info about the brand and product. Please make the custom packacking in dutch ( MAKE IN DUTCH)

Target Market(s)

See Brankbook

Industry/Entity Type

See Brankbook

Colors
00AB8E
00BBA5
67D7C9
C6EFE9
E9F9F6

Requirements
Must have
• See Brankbook
Nice to have
• See Brankbook
Should not have
• See Brankbook

```html
<!DOCTYPE html>
<html lang="nl">
<head>
<meta charset="utf-8">
<title>Quiet Porch – Wespen Lijmval verpakking</title>
<link rel="stylesheet" href="https://fonts.googleapis.com/css2?family=Poppins:wght@300;400;600;700&display=swap">
<style>
  :root {
    --green: #1fa55c;
    --green-dark: #155e37;
    --die: #2b9fe3;
    --paper: #ffffff;
    --stop-red: #d8232a;
    --trap-yellow: #f0e52a;
    --trap-green: #6fae2e;
  }
  html, body { margin: 0; padding: 0; }
  body {
    width: 686px; height: 1200px; overflow: hidden;
    background: var(--paper);
    font-family: "Poppins", sans-serif;
  }
  .dieline { position: absolute; left: 0; top: 300px; width: 686px; height: 588px; }
  .cut { fill: none; stroke: var(--die); stroke-width: 2; }
  .fold { fill: none; stroke: var(--die); stroke-width: 2; stroke-dasharray: 60 14; }
  .panel-white { fill: var(--paper); }
  .panel-green { fill: var(--green); }
  .badge { fill: var(--green-dark); stroke: #fff; stroke-width: 3; }
  .brand-name { font-weight: 600; font-size: 26px; fill: var(--green-dark); }
  .brand-dot { fill: var(--green); }
  .title { font-weight: 700; font-size: 60px; fill: var(--green-dark); letter-spacing: -1px; }
  .subtitle { font-weight: 300; font-size: 50px; fill: var(--green); }
  .bullet { font-weight: 400; font-size: 18px; fill: var(--green); }
  .count-num { font-weight: 600; font-size: 58px; fill: #fff; }
  .count-word { font-weight: 600; font-size: 22px; fill: #fff; }
  .side-copy { font-weight: 400; font-size: 17px; fill: #fff; }
  .side-name { font-weight: 600; font-size: 15px; fill: #fff; }
  .tagline-top { font-weight: 700; font-size: 32px; fill: var(--green-dark); }
  .tagline-bottom { font-weight: 700; font-size: 32px; fill: var(--green); }
  .stop-ring { fill: #fff; stroke: var(--stop-red); stroke-width: 3.5; }
  .stop-bar { stroke: var(--stop-red); stroke-width: 3.5; }
</style>
</head>
<body>
<svg class="dieline" viewBox="100 1300 1260 1080" xmlns="http://www.w3.org/2000/svg">
  <defs>
    <linearGradient id="trapFill" x1="0" y1="0" x2="1" y2="1">
      <stop offset="0" stop-color="#f3ea2e"/>
      <stop offset="0.5" stop-color="#9cc73a"/>
      <stop offset="1" stop-color="#4f9a2c"/>
    </linearGradient>
    <g id="stopSign">
      <circle class="stop-ring" r="18"/>
      <line class="stop-bar" x1="-12.7" y1="-12.7" x2="12.7" y2="12.7"/>
    </g>
    <g id="frontPanel">
      <rect class="panel-white" x="0" y="0" width="427" height="695"/>
      <rect x="267" y="155" width="160" height="540" fill="url(#trapFill)" role="img" aria-label="Foto van de gele wespenval met gevangen insecten"/>
      <rect x="301" y="0" width="82" height="98" class="panel-green"/>
      <text class="count-num" x="342" y="63" text-anchor="middle">2</text>
      <text class="count-word" x="342" y="90" text-anchor="middle">STUKS</text>
      <circle class="brand-dot" cx="52" cy="72" r="14"/>
      <text class="brand-name" x="76" y="81">Quiet Porch</text>
      <text class="title" x="34" y="312">Wespen</text>
      <text class="subtitle" x="34" y="362">Lijmval</text>
      <text class="bullet" x="34" y="525">• Super effectief</text>
      <text class="bullet" x="34" y="544">• Click in systeem</text>
      <text class="bullet" x="34" y="563">• Lichtgevend in donker</text>
      <use href="#stopSign" x="53" y="641"/>
      <use href="#stopSign" x="109" y="641"/>
      <use href="#stopSign" x="162" y="641"/>
    </g>
  </defs>

  <!-- panels -->
  <use href="#frontPanel" x="158" y="1535"/>
  <use href="#frontPanel" x="752" y="1535"/>

  <g class="side-badges">
    <rect class="panel-green" x="585" y="1535" width="167" height="695"/>
    <circle class="badge" cx="670" cy="1660" r="45"/>
    <circle class="badge" cx="670" cy="1778" r="45"/>
    <circle class="badge" cx="670" cy="1900" r="45"/>
    <circle class="badge" cx="670" cy="2020" r="45"/>
    <text class="side-name" x="670" y="2165" text-anchor="middle">Quiet Porch</text>
  </g>

  <g class="side-story">
    <rect class="panel-green" x="1180" y="1535" width="163" height="695"/>
    <text class="side-copy" text-anchor="middle">
      <tspan x="1262" y="1742">Bij Quiet</tspan>
      <tspan x="1262" y="1761">Porch</tspan>
      <tspan x="1262" y="1780">hechten we</tspan>
      <tspan x="1262" y="1799">waarde aan</tspan>
      <tspan x="1262" y="1818">effectieve</tspan>
      <tspan x="1262" y="1837">bestrijding , om</tspan>
      <tspan x="1262" y="1856">de veiligheid</tspan>
      <tspan x="1262" y="1875">van iedereen</tspan>
      <tspan x="1262" y="1894">in jouw</tspan>
      <tspan x="1262" y="1913">omgeving te</tspan>
      <tspan x="1262" y="1932">garanderen</tspan>
    </text>
    <text class="side-name" x="1262" y="2165" text-anchor="middle">Quiet Porch</text>
  </g>

  <g class="lid-tagline" transform="rotate(180 362 1452)">
    <text class="tagline-bottom" x="259" y="1442">Protecting</text>
    <text class="tagline-top" x="259" y="1480">What Matters</text>
  </g>

  <!-- cut lines -->
  <path class="cut" d="M158 1370 L158 1360 Q165 1325 195 1325 L545 1325 Q578 1325 585 1360 L585 1370"/>
  <path class="cut" d="M158 1370 L158 2230 M585 1370 L585 1535"/>
  <path class="cut" d="M158 1535 L112 1548 L112 2215 L158 2230"/>
  <path class="cut" d="M590 1535 L590 1432 L724 1432 L740 1515 L745 1535"/>
  <path class="cut" d="M920 1582 L920 1505 Q920 1493 932 1493 L998 1493 Q1010 1493 1010 1505 L1010 1582"/>
  <path class="cut" d="M1343 1535 L1340 1432 L1207 1432 L1190 1515 L1183 1535"/>
  <path class="cut" d="M1343 1535 L1343 2230"/>
  <path class="cut" d="M160 2230 L160 2358 L240 2358 L240 2335 Q240 2313 262 2313 L478 2313 Q500 2313 500 2335 L500 2358 L580 2358 L580 2230"/>
  <path class="cut" d="M590 2230 L670 2310 L670 2340 Q670 2358 688 2358 L750 2358 L750 2230"/>
  <path class="cut" d="M755 2230 L838 2313 L838 2340 Q838 2358 856 2358 L1075 2358 Q1093 2358 1093 2340 L1093 2313 L1176 2230"/>
  <path class="cut" d="M1181 2230 L1181 2358 L1240 2358 Q1258 2358 1258 2340 L1258 2313 L1341 2230"/>
  <!-- fold lines -->
  <path class="fold" d="M158 1370 L585 1370 M158 1535 L1343 1535 M158 2230 L1343 2230"/>
  <path class="fold" d="M585 1535 L585 2230 M752 1535 L752 2230 M1180 1535 L1180 2230"/>
</svg>
</body>
</html>
```